Distribution company seeks to update marketing Brochure/Collateral

Want to take our existing mock-up in ppt format and convert to a more professional layout/design. This is a single sheet, two sided document to be given to prospective customers. File should be in a format ready to send to a printer. Take the text content we have provided and put it into an appealing format with whatever images are required to visually convey our message.
Target Market(s)
Manufacturing, Food Processing, Retail Chains, Banks
Industry/Entity Type
Marketing
Font styles to use
Serif
Other font styles liked:
- Use Font in submitted documents or similar
Requirements
Must have
- Graphics should be representative of a distribution company

```html
<!DOCTYPE html>
<html lang="en">
<head>
<meta charset="utf-8">
<title>Harbor Point Supply – Two-Sided Sales Sheet</title>
<link rel="stylesheet" href="https://fonts.googleapis.com/css2?family=Source+Sans+3:ital,wght@0,400;0,600;0,700;1,400&display=swap">
<style>
  :root{
    --charcoal:#3b3c3e;
    --charcoal-soft:#4a4b4d;
    --slate:#7088a6;
    --slate-deep:#5d7593;
    --mist:#d6d7d8;
    --mist-light:#e4e5e6;
    --panel:#c4c5c7;
    --paper:#ffffff;
    --teal:#2a8b97;
    --ink:#2e2f31;
    --backdrop:#ebe8e3;
    --warm-1:#8a6a48;
    --warm-2:#d9cdb8;
  }
  *{box-sizing:border-box;margin:0;padding:0}
  html,body{width:1200px;height:675px;overflow:hidden}
  body{background:var(--backdrop);font-family:"Source Sans 3",sans-serif;color:var(--ink);position:relative}
  .sheet{position:absolute;top:40px;width:460px;height:595px;background:var(--mist);overflow:hidden;box-shadow:0 2px 8px rgba(0,0,0,.12)}
  .sheet--front{left:110px}
  .sheet--back{left:630px}
  .block{position:absolute}
  ul{list-style:none}

  /* front */
  .hero-photo{left:0;top:0;width:180px;height:205px;background:linear-gradient(160deg,var(--warm-2) 0%,var(--warm-1) 55%,#4d3a28 100%)}
  .masthead{left:180px;top:0;width:280px;height:205px;background:var(--mist-light);padding:12px 18px}
  .site-url{font-size:11px;color:var(--charcoal);border-bottom:1px solid #9fa1a4;padding-bottom:3px;display:inline-block}
  .brand-name{font-size:17px;font-weight:600;color:var(--slate-deep);letter-spacing:.06em;text-transform:uppercase;margin-top:18px;text-align:center}
  .brand-tagline{font-size:9.5px;color:var(--slate-deep);text-align:center;margin-top:1px}
  .headline{font-size:15.5px;line-height:1.2;color:var(--charcoal);text-align:center;margin-top:22px}
  .intro-band{left:0;top:205px;width:460px;height:62px;background:var(--charcoal-soft);color:#f1f1f1;font-size:8.6px;line-height:1.35;padding:10px 14px}
  .issues{left:0;top:300px;width:162px;height:255px;background:var(--slate);color:#fff;padding:14px 12px}
  .issues h3{font-size:10.5px;font-weight:600;line-height:1.2;color:var(--ink);margin-bottom:10px}
  .issues li{font-size:8.2px;line-height:1.25;margin-bottom:4px;padding-left:8px;position:relative}
  .issues li::before{content:"•";position:absolute;left:0}
  .challenges{left:176px;top:276px;width:276px}
  .challenges h3{font-size:11.5px;font-weight:700;color:var(--charcoal);margin-bottom:6px}
  .check-grid{display:grid;grid-template-columns:1fr 1fr;gap:5px 10px}
  .check-item{display:flex;gap:4px;font-size:7.8px;line-height:1.2;color:var(--charcoal)}
  .check-item svg{flex:0 0 12px}
  .help-panel{left:176px;top:370px;width:276px;height:178px;background:var(--panel);padding:6px 8px}
  .help-panel h3{font-size:13px;font-weight:600;text-align:center;color:var(--charcoal);margin-bottom:5px}
  .service-grid{display:grid;grid-template-columns:repeat(3,1fr);gap:6px}
  .service{font-size:6.6px;line-height:1.2}
  .service-title{background:var(--charcoal);color:#fff;font-size:7.6px;text-align:center;padding:3px 2px}
  .service-desc{background:var(--slate);color:#fff;text-align:center;padding:3px}
  .mini-brand{position:absolute;font-size:6.5px;font-weight:600;letter-spacing:.05em;text-transform:uppercase;color:var(--charcoal)}
  .footer{left:0;top:555px;width:460px;height:40px;background:var(--charcoal);color:#d8d8d8;font-size:7.6px;line-height:1.3;padding:7px 14px}

  /* back */
  .platform-col{left:0;top:0;width:190px;height:555px;background:var(--slate);color:#fff;padding:32px 16px}
  .platform-col h3{font-size:9.5px;font-weight:600;color:var(--ink);margin-bottom:8px;line-height:1.2}
  .platform-col li{font-size:8px;line-height:1.25;margin-bottom:5px;padding-left:8px;position:relative}
  .platform-col li::before{content:"•";position:absolute;left:0}
  .divider{border-top:1px solid rgba(255,255,255,.5);margin:12px 0}
  .platform-head{left:190px;top:0;width:270px;height:24px;background:var(--charcoal);color:#fff;font-size:10.5px;font-weight:600;text-align:center;line-height:24px}
  .platform-features{left:190px;top:24px;width:270px;height:112px;background:#cfd0d2}
  .screen-preview{position:absolute;left:14px;top:22px;width:110px;height:64px;background:linear-gradient(180deg,#f4f6f9,#c9d4e2);border:1px solid #a8afb8}
  .feature-list{position:absolute;left:134px;top:8px;width:128px}
  .feature-list li{display:flex;gap:3px;font-size:6.8px;line-height:1.15;margin-bottom:3px;color:var(--charcoal)}
  .feature-list svg{flex:0 0 9px}
  .brand-block{left:190px;top:136px;width:270px;height:110px;background:var(--paper);padding-top:30px;text-align:center}
  .brand-block .brand-name{font-size:22px;color:var(--charcoal);margin-top:0;letter-spacing:.08em}
  .brand-block .brand-tagline{font-size:12px;color:var(--charcoal)}
  .consolidate{left:190px;top:246px;width:270px;height:40px;background:var(--charcoal);color:#fff;font-size:11.5px;line-height:1.2;text-align:right;padding:7px 14px}
  .print-detail{left:190px;top:286px;width:270px;height:269px;background:#cfd0d2}
  .print-specs{position:absolute;right:14px;top:10px;text-align:right;font-size:9.5px;line-height:1.3;color:var(--charcoal)}
  .print-photo{position:absolute;left:12px;top:56px;width:96px;height:64px;border-radius:50%;background:radial-gradient(circle at 40% 40%,#e8c35a,#c9503c 55%,#3f7d6c)}
  .certified-pill{position:absolute;left:66px;top:66px;width:196px;height:34px;background:var(--teal);color:#fff;border-radius:10px;font-size:9px;line-height:1.2;padding:5px 10px 5px 46px}
</style>
</head>
<body>

<section class="sheet sheet--front" aria-label="Sales sheet front">
  <div class="block hero-photo" role="img" aria-label="Photo of a warehouse aisle with stacked boxes on tall shelving"></div>
  <header class="block masthead">
    <span class="site-url">www.yoursitehere.com</span>
    <p class="brand-name">Harbor Point Supply</p>
    <p class="brand-tagline">Packaging • Printing • Distribution</p>
    <h1 class="headline">Time spent on procurement<br>is time that could be better<br>spent growing your business.</h1>
  </header>
  <p class="block intro-band">Harbor Point Supply is your Single Source Solution partner for everything you need to operate your business. From general supplies to packaging and retail support including full-service flexographic printing, Harbor Point Supply can meet your demands while reducing costs and improving efficiency every day.</p>

  <aside class="block issues">
    <h3>Have you experienced any of these issues with your current supplier?</h3>
    <ul>
      <li>Frequent backorders or lack of sufficient inventory</li>
      <li>Billing Errors</li>
      <li>Long Lead Times</li>
      <li>High Minimum order amounts</li>
      <li>Inability to source correct products</li>
      <li>Simply taking your orders without adding value or offering better solutions</li>
      <li>Difficulty in ordering process</li>
      <li>Poor Customer Service</li>
      <li>Inability to deliver product when and where needed</li>
      <li>Inflexibility</li>
    </ul>
  </aside>

  <div class="block challenges">
    <h3>We understand your procurement challenges.</h3>
    <div class="check-grid">
      <p class="check-item"><svg width="12" height="12" viewBox="0 0 12 12"><rect x=".5" y=".5" width="11" height="11" fill="#fff" stroke="#3b3c3e"/><path d="M2.5 6l2.5 2.5 5-6" fill="none" stroke="#5d7593" stroke-width="1.8"/></svg>Are you managing purchases with multiple vendors across multiple locations, departments or business units?</p>
      <p class="check-item"><svg width="12" height="12" viewBox="0 0 12 12"><rect x=".5" y=".5" width="11" height="11" fill="#fff" stroke="#3b3c3e"/><path d="M2.5 6l2.5 2.5 5-6" fill="none" stroke="#5d7593" stroke-width="1.8"/></svg>Would you like to lower your indirect supply spend across multiple categories and suppliers?</p>
      <p class="check-item"><svg width="12" height="12" viewBox="0 0 12 12"><rect x=".5" y=".5" width="11" height="11" fill="#fff" stroke="#3b3c3e"/><path d="M2.5 6l2.5 2.5 5-6" fill="none" stroke="#5d7593" stroke-width="1.8"/></svg>Would you like to consolidate your indirect supply purchases on one time-saving order platform?</p>
      <p class="check-item"><svg width="12" height="12" viewBox="0 0 12 12"><rect x=".5" y=".5" width="11" height="11" fill="#fff" stroke="#3b3c3e"/><path d="M2.5 6l2.5 2.5 5-6" fill="none" stroke="#5d7593" stroke-width="1.8"/></svg>Would you like to prevent spending abuse?</p>
    </div>
  </div>

  <div class="block help-panel">
    <h3>How can Harbor Point help?</h3>
    <div class="service-grid">
      <div class="service"><p class="service-title">Sourcing and Procurement Support</p><p class="service-desc">Let us manage your suppliers while you focus on your business, saving money and time</p></div>
      <div class="service"><p class="service-title">Warehousing and Fulfillment</p><p class="service-desc">Our distribution center allows us to efficiently manage fulfillment and delivery of supplies</p></div>
      <div class="service"><p class="service-title">Inventory Management</p><p class="service-desc">We allow our customers to remain competitive while avoiding overstock and shortages</p></div>
      <div class="service"><p class="service-title">Specialty Printing</p><p class="service-desc">SQF certified manufacturer of plain and printed labels up to 8 colors</p></div>
      <div class="service"><p class="service-title">Integrated IT Order Management</p><p class="service-desc">Customer-specific reporting and web ordering allow you to conduct business at your convenience</p></div>
      <div class="service"><p class="service-title">Packaging</p><p class="service-desc">From common corrugated to specialized, custom product packaging</p></div>
    </div>
    <p class="mini-brand" style="right:10px;bottom:6px">Harbor Point Supply</p>
  </div>

  <footer class="block footer">
    <p>1420 Harborview Lane,<br>Suite 6 Riverton, FL 32000<br>Phone (555) 014 - 2278</p>
  </footer>
</section>

<section class="sheet sheet--back" aria-label="Sales sheet back">
  <aside class="block platform-col">
    <h3>What can our Web platform do for you?</h3>
    <ul>
      <li>Make purchasing easier</li>
      <li>Control your spend and improve cash flow</li>
      <li>Prevent spending abuse</li>
      <li>Identify trends and patterns</li>
      <li>Gain purchasing efficiencies with real-time order tracking</li>
      <li>Manage multiple business units or locations with ease</li>
    </ul>
    <div class="divider"></div>
    <h3>Better supply chain performance and value with Harbor Point Supply</h3>
    <ul>
      <li>Cost Reduction on Direct and Indirect spend</li>
      <li>Strategic Sourcing – access to our network of suppliers for specialty items unique to your industry</li>
      <li>Seamless ordering of large quantity items without inventory holding costs, reducing working capital and preventing overstocking and supply shortage</li>
      <li>Better Management, Control, and purchasing analysis</li>
      <li>Ease of ordering through proprietary online ordering system (Web View), FTP, file transfer and EDI</li>
    </ul>
  </aside>

  <h2 class="block platform-head">Web Platform Design</h2>
  <div class="block platform-features">
    <div class="screen-preview" role="img" aria-label="Screenshot of the online ordering storefront"></div>
    <ul class="feature-list">
      <li><svg width="9" height="9" viewBox="0 0 9 9"><path d="M1 4.5l2.3 2.3L8 1.5" fill="none" stroke="#5d7593" stroke-width="1.8"/></svg>User-friendly storefront Web interface</li>
      <li><svg width="9" height="9" viewBox="0 0 9 9"><path d="M1 4.5l2.3 2.3L8 1.5" fill="none" stroke="#5d7593" stroke-width="1.8"/></svg>Each user has their own User ID and password</li>
      <li><svg width="9" height="9" viewBox="0 0 9 9"><path d="M1 4.5l2.3 2.3L8 1.5" fill="none" stroke="#5d7593" stroke-width="1.8"/></svg>Purchases are mapped to the particular User/Department</li>
      <li><svg width="9" height="9" viewBox="0 0 9 9"><path d="M1 4.5l2.3 2.3L8 1.5" fill="none" stroke="#5d7593" stroke-width="1.8"/></svg>Dashboard allows User to quickly review most current order and previous orders</li>
      <li><svg width="9" height="9" viewBox="0 0 9 9"><path d="M1 4.5l2.3 2.3L8 1.5" fill="none" stroke="#5d7593" stroke-width="1.8"/></svg>Communicate messages to users via the website</li>
      <li><svg width="9" height="9" viewBox="0 0 9 9"><path d="M1 4.5l2.3 2.3L8 1.5" fill="none" stroke="#5d7593" stroke-width="1.8"/></svg>Chat with HPS Customer Support regarding your orders</li>
    </ul>
  </div>

  <div class="block brand-block">
    <p class="brand-name">Harbor Point Supply</p>
    <p class="brand-tagline">Packaging • Printing • Distribution</p>
  </div>
  <h2 class="block consolidate">Consolidate: We Also Offer Full Service<br>In-house Flexographic Printing</h2>

  <div class="block print-detail">
    <p class="print-specs">Up to 8 colors<br>Paper, Synthetic Label, Tags,<br>BOPP, +Others</p>
    <div class="certified-pill">Fully Integrated, SQF Certified<br>Flexographic Printing</div>
    <div class="print-photo" role="img" aria-label="Photo of colorful printed labels and packaging samples"></div>
    <p class="mini-brand" style="right:12px;bottom:10px">Harbor Point Supply</p>
  </div>

  <footer class="block footer">
    <p>1420 Harborview Lane,<br>Suite 6 Riverton, FL 32000<br>Phone (555) 014 - 2278</p>
  </footer>
</section>

</body>
</html>
```